Email Signiture and letterhead design

we are looking for a modern business design to incorporate our logo and qel certification plus social icons for Vorlant, Pelmora, and zandoro
they must include our UK vat and also company registration as text but I can fill these out. Email signature to have a link/icon to our webshop www.trexolan.co.uk

Target Market(s)

All

Font styles to use
Serif
Sans Serif

Requirements
Must have
• Address, tel, email , web details incorperated
Nice to have
• a professional looking letter head and email signiture, Email signature to have a link/icon to our webshop www.trexolan.co.uk

```html
<!DOCTYPE html>
<html lang="en">
<head>
<meta charset="utf-8">
<title>Trexolan Hubs &amp; Bearings – Letterhead &amp; Email Signatures</title>
<link href="https://fonts.googleapis.com/css2?family=Questrial&family=Tinos&display=swap" rel="stylesheet">
<style>
  :root {
    --red: #ed1c24;
    --ink: #333333;
    --grey-text: #555555;
    --paper: #f7f5f6;
    --stage-light: #b9b9b9;
    --stage-dark: #7d7d7d;
    --white: #ffffff;
    --black: #111111;
  }
  * { box-sizing: border-box; margin: 0; padding: 0; }
  html, body { width: 1200px; height: 784px; overflow: hidden; }
  body {
    position: relative;
    background: radial-gradient(ellipse at 60% 45%, var(--stage-light), var(--stage-dark));
    font-family: "Questrial", sans-serif;
    color: var(--ink);
  }
  .sheet {
    position: absolute;
    background: var(--paper);
    box-shadow: 0 2px 10px rgba(0,0,0,.35);
    overflow: hidden;
  }
  .caption {
    position: absolute;
    font-family: "Tinos", serif;
    font-size: 11.5px;
    color: #1c1c1c;
    transform: translateX(-50%);
    white-space: nowrap;
  }
  .brand { position: absolute; text-align: center; }
  .brand-dot {
    display: inline-block;
    border-radius: 50%;
    border: 3px solid var(--red);
  }
  .brand-name {
    display: block;
    color: var(--red);
    letter-spacing: .04em;
    text-transform: uppercase;
    white-space: nowrap;
  }
  .social { position: absolute; display: flex; gap: 4px; align-items: center; }
  .social-dot { width: 14px; height: 14px; border-radius: 50%; background: var(--red); }
  .link-icon { position: absolute; }
  .contact-line { display: flex; align-items: center; gap: 4px; white-space: nowrap; }
  .contact-line svg { flex: none; }
  .footer-band { position: absolute; left: 0; bottom: 0; width: 100%; }
  .footer-text {
    position: absolute; left: 0; width: 100%;
    text-align: center; color: var(--white); white-space: nowrap;
  }

  /* Letterhead */
  .letterhead { left: 64px; top: 53px; width: 471px; height: 664px; }
  .letterhead .social { left: 398px; top: 20px; }
  .letterhead .brand { left: 0; width: 100%; top: 26px; }
  .letterhead .brand-dot { width: 30px; height: 30px; }
  .letterhead .brand-name { font-size: 12px; margin-top: 6px; }
  .letter-body { position: absolute; left: 55px; top: 154px; width: 359px; font-family: "Tinos", serif; color: #3a3a3a; }
  .greeting { font-size: 14px; margin-bottom: 22px; }
  .letter-body p.para { font-size: 7.5px; line-height: 11.3px; text-align: justify; margin-bottom: 11.5px; }
  .closing { font-size: 7.5px; margin-top: 22px; }
  .signature-mark { position: absolute; left: 60px; top: 473px; width: 62px; height: 26px; background: linear-gradient(90deg, rgba(30,30,40,.15), rgba(30,30,40,.35), rgba(30,30,40,.1)); border-radius: 40% 10% 40% 10%; }
  .signer { position: absolute; left: 59px; top: 503px; }
  .signer-name { font-size: 10.5px; color: #444; }
  .signer-role { font-size: 8px; color: #555; margin-top: 2px; }
  .letterhead .footer-band { height: 84px; }
  .letterhead .footer-text { font-size: 8.8px; line-height: 10.5px; }
  .letterhead .line-one { top: 636px; display: flex; justify-content: center; gap: 4px; align-items: center; }
  .letterhead .line-two { top: 647px; }

  /* Email signatures */
  .signature-one { left: 612px; top: 183px; width: 489px; height: 90px; }
  .signature-one .brand { left: 6px; top: 10px; width: 176px; }
  .signature-one .brand-dot { width: 28px; height: 28px; }
  .signature-one .brand-name { font-size: 10px; margin-top: 6px; }
  .signature-one .address { position: absolute; left: 208px; top: 18px; font-size: 8.8px; line-height: 11.4px; color: var(--grey-text); }
  .signature-one .social { left: 327px; top: 14px; }
  .signature-one .contacts { position: absolute; left: 326px; top: 37px; font-size: 8.8px; line-height: 12.5px; color: var(--grey-text); }
  .signature-one .link-icon { left: 456px; top: 11px; }
  .signature-one .footer-band { height: 24px; }

  .signature-two { left: 612px; top: 365px; width: 486px; height: 153px; }
  .signature-two .brand { left: 26px; top: 18px; width: 160px; }
  .signature-two .brand-dot { width: 30px; height: 30px; }
  .signature-two .brand-name { font-size: 10.5px; margin-top: 6px; }
  .signature-two .social { left: 393px; top: 22px; }
  .signature-two .link-icon { left: 450px; top: 20px; }
  .signature-two .contacts { position: absolute; left: 27px; top: 86px; font-size: 9px; line-height: 12.5px; color: var(--grey-text); }
  .signature-two .footer-band { height: 44px; }
  .signature-two .footer-text { top: 134px; font-size: 9px; }
</style>
</head>
<body>

  <!-- Letterhead -->
  <section class="sheet letterhead">
    <div class="social" aria-label="Vorlant, zandoro and Pelmora profiles">
      <span class="social-dot"></span><span class="social-dot"></span><span class="social-dot"></span>
    </div>
    <div class="brand">
      <span class="brand-dot"></span>
      <span class="brand-name">Trexolan Hubs &amp; Bearings Ltd</span>
    </div>

    <div class="letter-body">
      <p class="greeting">Dear Mr. Daniel Harwick,</p>
      <p class="para">Lorem ipsum dolor sit amet, consectetur adipiscing elit. Donec orci purus, luctus vitae dignissim eu, iaculis sed purus. Vivamus faucibus, ipsum nec aliquet viverra, leo mauris condimentum ligula, sit amet sagittis enim ligula quis arcu. Nam egestas tortor id nisi porttitor mattis. In tortor ante, ultricies in suscipit a, tempus non massa. Vivamus et auctor mi. Fusce vel massa nulla. Phasellus nec eros mauris, et scelerisque orci.</p>
      <p class="para">Donec malesuada orci vitae nulla accumsan porta a id massa. Quisque accumsan iaculis magna sit amet fringilla. Maecenas consequat, magna eget tincidunt semper, odio nibh rutrum mi, id feugiat ante nisi eu risus. Vestibulum nunc orci, rhoncus a placerat in, ultricies in mi. Cras mattis varius eros, vel fringilla nisi suscipit eget. Quisque scelerisque sagittis nulla at porttitor.</p>
      <p class="para">Sed id augue vitae urna euismod commodo aliquet a quam. Pellentesque arcu velit, cursus et malesuada ut, consequat et diam. Nullam erat sem, rhoncus id ullamcorper vitae, rhoncus et arcu. In ultricies ultricies nulla, ut rutrum nisi iaculis at. Donec eu magna a metus ornare faucibus. Fusce aliquet faucibus ultricies. Morbi semper, est id tincidunt gravida, sem arcu adipiscing lacus, ac bibendum nulla leo eu purus. Quisque nec diam sed risus consectetur a accumsan quis quis nibh. Vestibulum id purus lorem.</p>
      <p class="para">It is a long established fact that a reader will be distracted by the readable content of a page when looking at its layout. The point of using Lorem Ipsum is that it has a more-or-less normal distribution of letters, as opposed to using 'Content here, content here', making it look like readable English. Many desktop publishing packages</p>
      <p class="closing">Sincerely,</p>
    </div>

    <div class="signature-mark" role="img" aria-label="Handwritten signature of Daniel Harwick"></div>
    <div class="signer">
      <p class="signer-name">Daniel Harwick</p>
      <p class="signer-role">President</p>
    </div>

    <svg class="footer-band" viewBox="0 0 471 84" preserveAspectRatio="none" aria-hidden="true">
      <path d="M0,84 L0,46 Q220,22 471,14 L471,84 Z" fill="var(--red)"/>
      <path d="M6,42 Q200,10 471,2 Q220,18 6,44 Z" fill="var(--black)"/>
    </svg>
    <p class="footer-text line-one">
      <svg width="8" height="8" viewBox="0 0 10 10" aria-hidden="true"><path d="M2,0 L4,3 L3,4 Q4,6 6,7 L7,6 L10,8 L8,10 Q3,10 0,2 Z" fill="var(--white)"/></svg>
      +44 (0) 161 555 0192
      <svg width="8" height="8" viewBox="0 0 10 10" aria-hidden="true"><circle cx="5" cy="5" r="4.3" fill="none" stroke="var(--white)" stroke-width="1.4"/><path d="M0.7,5 H9.3 M5,0.7 Q2,5 5,9.3 M5,0.7 Q8,5 5,9.3" fill="none" stroke="var(--white)" stroke-width="0.9"/></svg>
      www.trexolan.co.uk
    </p>
    <p class="footer-text line-two">VAT - XYZ-9B7788, Calder Row North, Brinsley, Manchester, M99 7QT</p>
  </section>
  <p class="caption" style="left:268px; top:730px;">Letterhead_01</p>

  <!-- Email signature 1 -->
  <section class="sheet signature-one">
    <div class="brand">
      <span class="brand-dot"></span>
      <span class="brand-name">Trexolan Hubs &amp; Bearings Ltd</span>
    </div>
    <p class="address">VAT - XYZ-9B7788<br>Calder Row North,<br>Brinsley,<br>Manchester, M99 7QT</p>
    <div class="social" aria-label="Vorlant, zandoro and Pelmora profiles">
      <span class="social-dot"></span><span class="social-dot"></span><span class="social-dot"></span>
    </div>
    <div class="contacts">
      <p class="contact-line"><svg width="8" height="8" viewBox="0 0 10 10" aria-hidden="true"><path d="M2,0 L4,3 L3,4 Q4,6 6,7 L7,6 L10,8 L8,10 Q3,10 0,2 Z" fill="var(--red)"/></svg>+44 (0) 161 555 0192</p>
      <p class="contact-line"><svg width="8" height="8" viewBox="0 0 10 10" aria-hidden="true"><circle cx="5" cy="5" r="5" fill="var(--red)"/><path d="M0.7,5 H9.3 M5,0.7 Q2,5 5,9.3 M5,0.7 Q8,5 5,9.3" fill="none" stroke="var(--white)" stroke-width="0.8"/></svg>www.trexolan.co.uk</p>
    </div>
    <svg class="link-icon" width="18" height="18" viewBox="0 0 20 20" aria-label="Webshop link">
      <g fill="none" stroke="#777" stroke-width="2" stroke-linecap="round">
        <path d="M8.5,11.5 L11.5,8.5"/>
        <path d="M9,5.5 L11.5,3 Q14,0.5 16.5,3 L17,3.5 Q19.5,6 17,8.5 L14.5,11"/>
        <path d="M11,14.5 L8.5,17 Q6,19.5 3.5,17 L3,16.5 Q0.5,14 3,11.5 L5.5,9"/>
      </g>
    </svg>
    <svg class="footer-band" viewBox="0 0 489 24" preserveAspectRatio="none" aria-hidden="true">
      <path d="M0,24 L0,9 Q240,4 489,2 L489,24 Z" fill="var(--red)"/>
      <path d="M2,8 Q240,0 489,0.5 Q240,3 2,9.5 Z" fill="var(--black)"/>
    </svg>
  </section>
  <p class="caption" style="left:848px; top:296px;">Email Signature_01</p>

  <!-- Email signature 2 -->
  <section class="sheet signature-two">
    <div class="brand">
      <span class="brand-dot"></span>
      <span class="brand-name">Trexolan Hubs &amp; Bearings Ltd</span>
    </div>
    <div class="social" aria-label="Vorlant, zandoro and Pelmora profiles">
      <span class="social-dot"></span><span class="social-dot"></span><span class="social-dot"></span>
    </div>
    <svg class="link-icon" width="18" height="18" viewBox="0 0 20 20" aria-label="Webshop link">
      <g fill="none" stroke="#777" stroke-width="2" stroke-linecap="round">
        <path d="M8.5,11.5 L11.5,8.5"/>
        <path d="M9,5.5 L11.5,3 Q14,0.5 16.5,3 L17,3.5 Q19.5,6 17,8.5 L14.5,11"/>
        <path d="M11,14.5 L8.5,17 Q6,19.5 3.5,17 L3,16.5 Q0.5,14 3,11.5 L5.5,9"/>
      </g>
    </svg>
    <div class="contacts">
      <p class="contact-line"><svg width="8" height="8" viewBox="0 0 10 10" aria-hidden="true"><path d="M2,0 L4,3 L3,4 Q4,6 6,7 L7,6 L10,8 L8,10 Q3,10 0,2 Z" fill="var(--red)"/></svg>+44 (0) 161 555 0192</p>
      <p class="contact-line"><svg width="8" height="8" viewBox="0 0 10 10" aria-hidden="true"><circle cx="5" cy="5" r="5" fill="var(--red)"/><path d="M0.7,5 H9.3 M5,0.7 Q2,5 5,9.3 M5,0.7 Q8,5 5,9.3" fill="none" stroke="var(--white)" stroke-width="0.8"/></svg>www.trexolan.co.uk</p>
    </div>
    <svg class="footer-band" viewBox="0 0 486 44" preserveAspectRatio="none" aria-hidden="true">
      <path d="M0,44 L0,18 Q240,8 486,1 L486,44 Z" fill="var(--red)"/>
      <path d="M6,16 Q240,2 486,0 Q240,6 6,18 Z" fill="var(--black)"/>
    </svg>
    <p class="footer-text">VAT - XYZ-9B7788, Calder Row North, Brinsley, Manchester, M99 7QT</p>
  </section>
  <p class="caption" style="left:847px; top:535px;">Email Signature_02</p>

</body>
</html>
```